Business Card Design for Mabel's Larder

We make food for dogs.
Business Card Design (using the logo designed by you). Our Brand color is a bright canary yellow. For example our signage is predominantly yellow, with the logo in black. I'd like the card also to use that imagery.
Feel free to use the two sides creatively.
Vertical Design is also great.

Industry/Entity Type

Pet food

Contact Information for Business Card

Name, email, website, phone no

Font styles to use
Sans Serif

Colors
59FF00
82FF00
B8FF75
E3FFCB
F4FFEA
FFF300
FFF600
FEFA6F
FFFEC7
FFFEE8

Requirements
Nice to have
• A graphic in the same brush stroke style of the logo shoeing a doggy bowl of food

```html
<!DOCTYPE html>
<html lang="en">
<head>
<meta charset="utf-8">
<title>Mabel's Larder – Business Card</title>
<link rel="stylesheet" href="https://fonts.googleapis.com/css2?family=Oswald:wght@500&family=Montserrat:wght@400;500&display=swap">
<style>
  :root {
    --page-bg: #e6e6e3;
    --card-black: #141414;
    --card-black-back: #111111;
    --canary: #fff300;
    --canary-soft: #f4e21a;
    --ink-light: #e9e9e9;
    --ink-muted: #cfcfcf;
    --gloss: #3a3a3a;
  }
  * { box-sizing: border-box; margin: 0; padding: 0; }
  html, body {
    width: 1200px; height: 1200px; overflow: hidden;
    background: var(--page-bg);
  }
  .sheet {
    width: 1200px; height: 1200px;
    display: flex; justify-content: center; align-items: center; gap: 64px;
  }
  .card {
    width: 480px; height: 768px;
    border-radius: 26px;
    position: relative;
    box-shadow: 0 18px 40px rgba(0,0,0,.25);
  }
  .card--front { background: var(--card-black); }
  .card--back { background: var(--card-black-back); }

  .wordmark {
    font-family: "Oswald", sans-serif;
    font-weight: 500;
    letter-spacing: 1px;
    text-transform: uppercase;
    text-align: center;
    white-space: nowrap;
  }
  .card--front .wordmark {
    position: absolute; left: 0; right: 0; top: 170px;
    font-size: 50px; color: var(--canary);
  }
  .card--back .wordmark {
    position: absolute; left: 0; right: 0; top: 350px;
    font-size: 54px; color: var(--gloss);
  }

  .holder {
    position: absolute; left: 0; right: 0; top: 320px; text-align: center;
  }
  .holder__name {
    font-family: "Oswald", sans-serif; font-weight: 500;
    font-size: 30px; letter-spacing: 2px; color: var(--canary);
    text-transform: uppercase;
  }
  .holder__title {
    font-family: "Montserrat", sans-serif; font-size: 16px;
    color: var(--ink-muted); margin-top: 2px;
  }

  .contact-divider {
    position: absolute; left: 70px; right: 70px; top: 430px;
    display: flex; align-items: center; gap: 14px;
  }
  .contact-divider__rule { flex: 1; height: 2px; background: var(--canary-soft); }
  .contact-divider__icons { display: flex; gap: 5px; }
  .icon-tile {
    width: 24px; height: 24px; border-radius: 5px;
    background: var(--canary); display: flex; align-items: center; justify-content: center;
  }

  .contact-list {
    position: absolute; left: 0; right: 0; top: 490px;
    text-align: center; list-style: none;
    font-family: "Montserrat", sans-serif; font-size: 17px; line-height: 27px;
    color: var(--ink-light);
  }

  .short-rule {
    position: absolute; left: 180px; right: 180px; top: 604px;
    height: 2px; background: var(--canary-soft);
  }

  .address {
    position: absolute; left: 0; right: 0; top: 640px;
    text-align: center; font-style: normal;
    font-family: "Montserrat", sans-serif; font-size: 17px; line-height: 27px;
    color: var(--ink-light);
  }
</style>
</head>
<body>
<main class="sheet">
  <section class="card card--front" aria-label="Card front">
    <h1 class="wordmark">Mabel's Larder</h1>

    <div class="holder">
      <p class="holder__name">Dana Whitfield</p>
      <p class="holder__title">Managing Director</p>
    </div>

    <div class="contact-divider">
      <span class="contact-divider__rule"></span>
      <span class="contact-divider__icons">
        <span class="icon-tile">
          <svg width="14" height="14" viewBox="0 0 24 24" aria-hidden="true"><path d="M6.6 10.8a15 15 0 0 0 6.6 6.6l2.2-2.2a1 1 0 0 1 1-.25 11.4 11.4 0 0 0 3.6.57 1 1 0 0 1 1 1V20a1 1 0 0 1-1 1A17 17 0 0 1 3 4a1 1 0 0 1 1-1h3.5a1 1 0 0 1 1 1c0 1.25.2 2.45.57 3.57a1 1 0 0 1-.25 1z" fill="#141414"/></svg>
        </span>
        <span class="icon-tile">
          <svg width="14" height="14" viewBox="0 0 24 24" aria-hidden="true"><rect x="2" y="5" width="20" height="14" rx="2" fill="#141414"/><path d="M3 6l9 7 9-7" stroke="#fff300" stroke-width="1.8" fill="none"/></svg>
        </span>
        <span class="icon-tile">
          <svg width="14" height="14" viewBox="0 0 24 24" aria-hidden="true"><circle cx="12" cy="12" r="9" fill="none" stroke="#141414" stroke-width="2.2"/><ellipse cx="12" cy="12" rx="4" ry="9" fill="none" stroke="#141414" stroke-width="1.8"/><path d="M3 12h18" stroke="#141414" stroke-width="1.8"/></svg>
        </span>
      </span>
      <span class="contact-divider__rule"></span>
    </div>

    <ul class="contact-list">
      <li>555-014-2290</li>
      <li>info@mabelslarder.com</li>
      <li>www.mabelslarder.com</li>
    </ul>

    <span class="short-rule"></span>

    <address class="address">
      18 Orchard Lane<br>
      Brookfield, NC 27000
    </address>
  </section>

  <section class="card card--back" aria-label="Card back">
    <p class="wordmark">Mabel's Larder</p>
  </section>
</main>
</body>
</html>
```